Google Form Graphic to suit our Brand and industry

Create a graphic / image for us to put at the top of our client enquiry google form.
The image will be a section of an architectural home with our branding over the top. Preferably translucent.
The image must suit the shape of the google forms image, which is an elongated rectangle
#003d5d - brand colour

Target Market(s)

residential home owners, high end architectural homes

Industry/Entity Type

Residential construction

Colors
0054AA
0677BA
7BADD7
CADEEF
E8F1F8

Requirements
Must have
• our branding and a photo of an architectural home in the background

```html
<!DOCTYPE html>
<html lang="en">
<head>
<meta charset="utf-8">
<title>New Client Enquiry Form</title>
<link rel="stylesheet" href="https://fonts.googleapis.com/css2?family=Roboto:wght@400;500&display=swap">
<style>
  :root {
    --page-bg: #ebeef1;
    --card-bg: #ffffff;
    --card-border: #dadce0;
    --brand-navy: #173f5f;
    --accent-band: #2b4d6d;
    --ink: #202124;
    --muted: #70757a;
    --required: #d93025;
    --name-ink: #ffffff;
    --sky-light: #f4f7fa;
    --sky-blue: #c9dcec;
    --facade: #e7eaee;
    --trees: #6f8d6a;
  }
  * { box-sizing: border-box; margin: 0; padding: 0; }
  html, body { width: 1194px; height: 1200px; overflow: hidden; }
  body {
    background: var(--page-bg);
    font-family: "Roboto", Arial, sans-serif;
    color: var(--ink);
    position: relative;
  }
  .form { position: absolute; left: 24px; width: 1153px; top: 18px; }
  .card {
    background: var(--card-bg);
    border: 1px solid var(--card-border);
    border-radius: 12px;
    overflow: hidden;
    position: relative;
    margin-bottom: 20px;
  }
  .banner { height: 288px; border: none; }
  .banner-photo {
    position: absolute; inset: 0;
    background:
      linear-gradient(90deg, var(--sky-light) 20%, rgba(255,255,255,0) 55%),
      linear-gradient(180deg, var(--sky-blue) 0%, var(--facade) 55%, var(--trees) 100%);
  }
  .banner-panel { position: absolute; inset: 0; }
  .brand-name {
    position: absolute; left: 34px; top: 131px;
    font-size: 25px; font-weight: 500; letter-spacing: 0.5px;
    color: var(--name-ink); line-height: 1;
  }
  .intro { height: 206px; padding: 51px 36px 0; }
  .intro::before {
    content: ""; position: absolute; left: 0; right: 0; top: 0; height: 15px;
    background: var(--accent-band);
  }
  .form-title { font-size: 42px; font-weight: 400; line-height: 1.2; }
  .form-description { font-size: 21px; margin-top: 36px; line-height: 1.4; }
  .question { height: 206px; padding: 38px 36px 0; }
  .question-label { font-size: 24px; line-height: 1.3; }
  .required { color: var(--required); margin-left: 4px; }
  .answer-field {
    width: 540px; margin-top: 39px; padding-bottom: 10px;
    font-size: 21px; color: var(--muted);
    border-bottom: 1px dotted #9aa0a6;
  }
</style>
</head>
<body>
  <main class="form">
    <header class="card banner">
      <div class="banner-photo" role="img" aria-label="Photograph of a modern white architectural home with pine trees under a pale blue sky"></div>
      <svg class="banner-panel" width="1153" height="288" viewBox="0 0 1153 288" aria-hidden="true">
        <polygon points="0,0 362,0 265,144 372,288 0,288" fill="var(--brand-navy)"/>
      </svg>
      <div class="brand-name">Brightmoor Homes</div>
    </header>

    <section class="card intro">
      <h1 class="form-title">New Client Enquiry Form</h1>
      <p class="form-description">We would love to hear your thought or feedback on how we can improve your experience !!</p>
    </section>

    <section class="card question">
      <p class="question-label">Firstly, how did you hear about us ?<span class="required">*</span></p>
      <div class="answer-field">Short answer text</div>
    </section>

    <section class="card question">
      <p class="question-label">Name</p>
      <div class="answer-field">Short answer text</div>
    </section>

    <section class="card question">
      <p class="question-label">Phone</p>
      <div class="answer-field">Short answer text</div>
    </section>
  </main>
</body>
</html>
```